Meridale Dental Business Card

Please design a professional but colorful looking business card. Our new logo is attached. The card also needs the following information:
For ALL Your Dental Needs
Curtis L. Hobbel, D.D.S.
620-555-0147
20463-C North Fernwick, Larkmoor, KS 74031
www.meridaledentalok.example

Industry/Entity Type

Business

Colors

Designer to choose colors to be used in the design.

```html
<!DOCTYPE html>
<html lang="en">
<head>
<meta charset="utf-8">
<title>Meridale Dental Business Card</title>
<link href="https://fonts.googleapis.com/css2?family=Questrial&display=swap" rel="stylesheet">
<style>
  :root {
    --backdrop: #3a3a3c;
    --card: #f7f7f7;
    --ink: #3b3d40;
    --ink-soft: #4a4c50;
    --blue: #1d5fa8;
    --green: #2fbf2a;
    --red: #d9380f;
    --white: #ffffff;
  }
  * { box-sizing: border-box; margin: 0; padding: 0; }
  html, body {
    width: 1200px;
    height: 900px;
    overflow: hidden;
  }
  body {
    background: var(--backdrop);
    font-family: "Questrial", "Century Gothic", sans-serif;
    position: relative;
  }
  .business-card {
    position: absolute;
    left: 75px;
    top: 150px;
    width: 1050px;
    height: 600px;
    background: var(--card);
    overflow: hidden;
  }
  .brand {
    position: absolute;
    left: 110px;
    top: 170px;
    display: flex;
    flex-direction: column;
    align-items: flex-start;
    gap: 18px;
  }
  .brand-square {
    width: 64px;
    height: 64px;
    border-radius: 10px;
    background: var(--blue);
  }
  .brand-name {
    color: var(--ink);
    font-size: 50px;
    line-height: 1.02;
    letter-spacing: 1px;
    text-transform: uppercase;
  }
  .divider {
    position: absolute;
    left: 480px;
    top: 90px;
    width: 2px;
    height: 310px;
    background: var(--blue);
  }
  .dentist-name {
    position: absolute;
    left: 530px;
    top: 88px;
    color: var(--ink);
    font-size: 31px;
    letter-spacing: 1px;
  }
  .contact {
    position: absolute;
    right: 90px;
    top: 190px;
    text-align: right;
    color: var(--ink-soft);
    font-size: 21px;
    line-height: 1.45;
    letter-spacing: 0.5px;
  }
  .website {
    position: absolute;
    right: 90px;
    top: 330px;
    color: var(--ink);
    font-size: 23px;
    letter-spacing: 1px;
  }
  .tab {
    position: absolute;
    bottom: 0;
    border-radius: 14px 14px 0 0;
  }
  .tab-green { left: 0; width: 135px; height: 75px; background: var(--green); border-top-left-radius: 0; }
  .tab-red { left: 150px; width: 130px; height: 100px; background: var(--red); }
  .tagline-band {
    position: absolute;
    left: 295px;
    right: 0;
    bottom: 0;
    height: 110px;
    background: var(--blue);
    border-radius: 14px 0 0 0;
    display: flex;
    align-items: center;
    padding-left: 40px;
  }
  .tagline {
    color: var(--white);
    font-size: 32px;
    letter-spacing: 7px;
  }
</style>
</head>
<body>
  <div class="business-card">
    <div class="brand">
      <div class="brand-square"></div>
      <div class="brand-name">Meridale<br>Dental</div>
    </div>

    <div class="divider"></div>

    <div class="dentist-name">Curtis L. Hobbel, D.D.S.</div>

    <div class="contact">
      <p>20463-C North Fernwick</p>
      <p>Larkmoor, KS 74031</p>
      <p>620-555-0147</p>
    </div>

    <div class="website">www.meridaledentalok.example</div>

    <div class="tab tab-green"></div>
    <div class="tab tab-red"></div>
    <div class="tagline-band">
      <p class="tagline">For ALL Your Dental Needs</p>
    </div>
  </div>
</body>
</html>
```